Cortelune Pamphlet

We need to design a pamplet for Cortelune, a Bespoke Wine Cellar design and build company. Our logo and signature cellar should be incorperated into the design (can be seen at www.cortelune-example.com). It should also include what will be called the template with a scematic drawing of a cellar to outline the key features An area called the process will showcase the different types of materials that can be used and there neesa to be indicative costs dependant in size also somewhere, as well as the fact that design £950+VAT but will be taken off the cost of the cellar if we do the job refunded back into project on approval.
.
Updates

Industry/Entity Type

It Company

```html
<!DOCTYPE html>
<html lang="en">
<head>
<meta charset="utf-8">
<title>Cortelune – Bespoke Wine Cellars</title>
<link href="https://fonts.googleapis.com/css2?family=Questrial&display=swap" rel="stylesheet">
<style>
  :root {
    --bg: #050505;
    --bg-soft: #0d0d0d;
    --white: #ffffff;
    --heading: #f2f2f2;
    --name: #cfcfcf;
    --body: #7d7d7d;
    --muted: #5f5f5f;
    --badge: #1b1b1b;
    --rule: #1e1e1e;
  }
  * { margin: 0; padding: 0; box-sizing: border-box; }
  html, body { width: 1200px; height: 849px; overflow: hidden; background: var(--bg); }
  body { font-family: "Questrial", "Century Gothic", sans-serif; color: var(--body); }

  .pamphlet {
    position: relative;
    width: 1200px; height: 849px;
    background: radial-gradient(ellipse at 30% 30%, var(--bg-soft), var(--bg) 70%);
    overflow: hidden;
  }
  .fold { position: absolute; top: 0; bottom: 0; width: 0; border-left: 2px dotted var(--rule); }
  .fold--one { left: 398px; }
  .fold--two { left: 796px; }

  .wordmark { position: absolute; left: 58px; top: 55px; font-size: 19px; letter-spacing: 4.5px; color: var(--white); text-transform: uppercase; }
  .tagline { position: absolute; left: 58px; top: 113px; font-size: 13px; color: var(--muted); }
  .city { position: absolute; left: 58px; top: 133px; font-size: 20px; color: var(--muted); }

  .intro { position: absolute; left: 58px; top: 224px; width: 281px; font-size: 12px; line-height: 21.2px; letter-spacing: 2px; color: var(--muted); text-align: justify; }
  .intro p { margin-bottom: 14px; }
  .intro .note { margin-top: 2px; font-size: 11px; }

  .plan-photo { position: absolute; left: 460px; top: 57px; width: 460px; height: 220px; background: linear-gradient(135deg, #f4f4f2 0%, #d9dad8 45%, #b8b9b6 100%); }

  .section-title { position: absolute; font-size: 17px; color: var(--heading); font-weight: 400; }
  .process-title { left: 460px; top: 332px; }
  .process-text { position: absolute; left: 460px; top: 365px; width: 470px; font-size: 12px; line-height: 21px; letter-spacing: 0.8px; color: var(--muted); }

  .template-title { right: 50px; top: 54px; }
  .template-text { position: absolute; left: 968px; top: 109px; width: 184px; font-size: 12px; line-height: 21.2px; letter-spacing: 1.6px; color: var(--muted); text-align: justify; }

  .brand-badge { position: absolute; left: 1015px; top: 350px; width: 185px; height: 50px; background: var(--badge); display: flex; align-items: center; padding-left: 20px; font-size: 14px; letter-spacing: 3.4px; color: var(--white); text-transform: uppercase; }

  .materials { position: absolute; top: 457px; }
  .materials--wood { left: 460px; }
  .materials--stone { left: 740px; }
  .materials--glass { left: 1015px; }
  .material { position: relative; height: 57px; width: 185px; }
  .material-name { display: block; font-size: 13px; color: var(--name); padding-top: -2px; }
  .material-spec { display: block; margin-top: 7px; font-size: 10px; color: var(--muted); }
  .swatch { position: absolute; left: 135px; top: 0; width: 50px; height: 50px; }

  .footer { position: absolute; left: 0; right: 0; top: 829px; text-align: center; font-size: 12px; letter-spacing: 0.5px; color: var(--muted); padding-right: 0; }
</style>
</head>
<body>
<main class="pamphlet">
  <span class="fold fold--one"></span>
  <span class="fold fold--two"></span>

  <div class="wordmark">Cortelune</div>
  <div class="tagline">Bespoke Wine Cellars</div>
  <div class="city">London</div>

  <section class="intro">
    <p>CORTELUNE combines custom artistic home wine cellar design with elegance and engineering to produce wine storage known for its extravagance, architecture and identity.</p>
    <p>Every bespoke wine cellar design is unique and individual according to your taste.</p>
    <p>Rich hard wood, hand stitched leather, a spiral wine cellar, beautiful lighting displays and seamless glass finish to display your magnificent collection of wines, champagnes and cigars...</p>
    <p>Bespoke Climate Controlled Wine Rooms and Home Wine Cellar Systems Installation With Humidity Control.</p>
    <p>The possibility of an climate controlled wine cellar for your wine storage may be the perfect way to increase the value of your home, in the way only a wine cellar can add.</p>
    <p>.....</p>
    <p class="note">Design costs of £950+VAT will be refunded back into the project opon approval.</p>
  </section>

  <div class="plan-photo" role="img" aria-label="Rolled architectural plans of a wine cellar at 1:50 scale"></div>

  <h2 class="section-title process-title">The Process</h2>
  <p class="process-text">Choose from our exclusive materials list, and have our luxury design team and specialist consultants come out and design your bespoke wine cellar today.</p>

  <h2 class="section-title template-title">The Template</h2>
  <p class="template-text">Rich hard wood, hand stitched leather, a spiral wine cellar, beautiful lighting displays and seamless glass finish to display your magnificent collection of wines, champagnes and cigars...</p>

  <div class="brand-badge">Cortelune</div>

  <ul class="materials materials--wood" style="list-style:none">
    <li class="material"><span class="material-name">Masur</span><span class="material-spec">Birch &nbsp;. &nbsp;00.00$ m2</span><span class="swatch" role="img" aria-label="Birch wood sample" style="background:linear-gradient(135deg,#c9995a,#a3733a)"></span></li>
    <li class="material"><span class="material-name">Carpathian</span><span class="material-spec">Elm &nbsp;. &nbsp;00.00$ m2</span><span class="swatch" role="img" aria-label="Elm wood sample" style="background:linear-gradient(135deg,#9b5a24,#6a3512)"></span></li>
    <li class="material"><span class="material-name">Zebrawood</span><span class="material-spec">Exotic &nbsp;. &nbsp;00.00$ m2</span><span class="swatch" role="img" aria-label="Zebrawood sample" style="background:linear-gradient(90deg,#d8b27a,#8c6238,#d8b27a,#8c6238,#d2ab73)"></span></li>
    <li class="material"><span class="material-name">Burmese</span><span class="material-spec">Exotic &nbsp;. &nbsp;00.00$ m2</span><span class="swatch" role="img" aria-label="Burmese wood sample" style="background:linear-gradient(135deg,#6d5b45,#43382a)"></span></li>
    <li class="material"><span class="material-name">Bocote</span><span class="material-spec">Exotic &nbsp;. &nbsp;00.00$ m2</span><span class="swatch" role="img" aria-label="Bocote wood sample" style="background:linear-gradient(135deg,#7a5530,#3e2713)"></span></li>
    <li class="material"><span class="material-name">Brownheart</span><span class="material-spec">Exotic &nbsp;. &nbsp;00.00$ m2</span><span class="swatch" role="img" aria-label="Brownheart wood sample" style="background:linear-gradient(135deg,#8a6e4a,#5e4a31)"></span></li>
  </ul>

  <ul class="materials materials--stone" style="list-style:none">
    <li class="material"><span class="material-name">Granada</span><span class="material-spec">Granite &nbsp;. &nbsp;00.00$ m2</span><span class="swatch" role="img" aria-label="Granite sample" style="background:linear-gradient(135deg,#bdb8b0,#8f8a83)"></span></li>
    <li class="material"><span class="material-name">Breccia Dark</span><span class="material-spec">Limestone &nbsp;. &nbsp;00.00$ m2</span><span class="swatch" role="img" aria-label="Dark limestone sample" style="background:linear-gradient(135deg,#d7b67c,#b08a4c)"></span></li>
    <li class="material"><span class="material-name">Breccia</span><span class="material-spec">Limestone &nbsp;. &nbsp;00.00$ m2</span><span class="swatch" role="img" aria-label="Limestone sample" style="background:linear-gradient(135deg,#c9a46a,#9b7641)"></span></li>
    <li class="material"><span class="material-name">Crema Marfil</span><span class="material-spec">Marble &nbsp;. &nbsp;00.00$ m2</span><span class="swatch" role="img" aria-label="Cream marble sample" style="background:linear-gradient(135deg,#9d8f73,#786b53)"></span></li>
    <li class="material"><span class="material-name">Emperador Dark</span><span class="material-spec">Marble &nbsp;. &nbsp;00.00$ m2</span><span class="swatch" role="img" aria-label="Dark marble sample" style="background:linear-gradient(135deg,#5a3a22,#2f1d10)"></span></li>
    <li class="material"><span class="material-name">Nero Maquena</span><span class="material-spec">Marble &nbsp;. &nbsp;00.00$ m2</span><span class="swatch" role="img" aria-label="Marble sample" style="background:linear-gradient(135deg,#d0a867,#a98046)"></span></li>
  </ul>

  <ul class="materials materials--glass" style="list-style:none">
    <li class="material"><span class="material-name">Atlantis</span><span class="material-spec">Glass &nbsp;. &nbsp;00.00$ m2</span><span class="swatch" role="img" aria-label="Textured glass sample" style="background:linear-gradient(135deg,#8e9a9c,#4f5a5c)"></span></li>
    <li class="material"><span class="material-name">Strata</span><span class="material-spec">Glass &nbsp;. &nbsp;00.00$ m2</span><span class="swatch" role="img" aria-label="Textured glass sample" style="background:linear-gradient(135deg,#7d8c8a,#4a5856)"></span></li>
    <li class="material"><span class="material-name">Eska</span><span class="material-spec">Glass &nbsp;. &nbsp;00.00$ m2</span><span class="swatch" role="img" aria-label="Textured glass sample" style="background:linear-gradient(135deg,#a7b4a6,#6b7a6c)"></span></li>
    <li class="material"><span class="material-name">Strialas</span><span class="material-spec">Glass &nbsp;. &nbsp;00.00$ m2</span><span class="swatch" role="img" aria-label="Textured glass sample" style="background:linear-gradient(135deg,#5f9a94,#2f5a56)"></span></li>
    <li class="material"><span class="material-name">Hitsu</span><span class="material-spec">Glass &nbsp;. &nbsp;00.00$ m2</span><span class="swatch" role="img" aria-label="Textured glass sample" style="background:linear-gradient(135deg,#7f918c,#3f4e4a)"></span></li>
    <li class="material"><span class="material-name">Grandeke</span><span class="material-spec">Glass &nbsp;. &nbsp;00.00$ m2</span><span class="swatch" role="img" aria-label="Textured glass sample" style="background:linear-gradient(135deg,#6c8c8c,#3a5050)"></span></li>
  </ul>

  <footer class="footer">www.cortelune-example.com &nbsp;. &nbsp;info@cortelune-example.com &nbsp;. &nbsp;Tel: &nbsp;0845 000 7291</footer>
</main>
</body>
</html>
```